Velvet Glow Co. Derma Roller packaging design

I need a box designed for a skin care brand called Velvet Glow Co. The box will be for our Derma Roller- a skin rejuvenation device. It will be sold online with lots of competition. I would like a modern, high end design, something that stands out and looks amazing. My logo is blush pink and black, for packaging i need no more than 3 colours, maybe gold if any other colour is used. A photo of a sample derma roller is attached below for an idea of what the product looks like, however my roller with have a clear handle with a black roller. The roller comes in a clear case, the box dimensions will need to be 16 cm long, 4 cm high, 4.5 cm wide.
ATTACHED ARE 2 SAMPLE BOXES AS AN EXAMPLE OF THE SIZE OF BOX REQUIRED!

Target Market(s)

25-50 year old women in the US

Colors
e667a6
000000
efefef

Requirements
Must have
• LOGO
• NAME OF PRODUCT- Cosmetic Derma Roller
• NEEDLE DEPTH- 0.25mm
• CAUTION- For personal use only, Do not use if allergic to metal, Do not use on open skin, wounds or active acne, sterilise roller before and after use.
Nice to have
• BENEFITS- Skin Rejuvenation, Collagen Induction Therapy, Increase product absorption, reduce acne scars and pigmentation
• FEATURES- 540 high quality titanium needles, ultra sharp needle tips, cross-line needle arrangement, ergonomic handle, anti slip grip,

```html
<!DOCTYPE html>
<html lang="en">
<head>
<meta charset="utf-8">
<title>Velvet Glow Co. Cosmetic Derma Roller – Packaging</title>
<link rel="stylesheet" href="https://fonts.googleapis.com/css2?family=Open+Sans:wght@400;600&display=swap">
<style>
  :root {
    --pink: #e0338a;
    --pink-soft: #f3c8dd;
    --pink-pale: #f7dbe8;
    --cream: #fbf6c8;
    --gold: #d89a1c;
    --gold-deep: #c9860f;
    --ink: #2b2b2b;
    --paper: #ffffff;
    --backdrop: #f1f1f1;
  }
  * { box-sizing: border-box; margin: 0; padding: 0; }
  html, body { width: 1200px; height: 1200px; overflow: hidden; }
  body {
    background: var(--backdrop);
    font-family: "Open Sans", Arial, sans-serif;
    color: var(--ink);
    position: relative;
  }
  .panel {
    position: absolute;
    left: 100px;
    width: 1000px;
    overflow: hidden;
  }

  /* Top panel – features */
  .panel--features {
    top: 150px;
    height: 240px;
    background: linear-gradient(90deg, var(--cream) 0%, var(--pink-pale) 60%, var(--pink-soft) 100%);
  }
  .product-photo {
    position: absolute;
    left: 300px; top: 60px;
    width: 400px; height: 120px;
    background: linear-gradient(90deg, rgba(60,60,60,.55) 0%, rgba(190,190,190,.45) 45%, rgba(245,245,245,.6) 100%);
  }
  .feature {
    position: absolute;
    font-size: 15px;
    line-height: 1.25;
    color: var(--ink);
  }
  .feature--needles { left: 60px; top: 52px; width: 200px; }
  .feature--tips { left: 60px; top: 110px; width: 200px; }
  .feature--arrangement { left: 60px; top: 160px; width: 200px; }
  .feature--handle { left: 760px; top: 56px; }
  .feature--grip { left: 760px; top: 160px; }
  .callouts { position: absolute; inset: 0; }

  /* Front panel */
  .panel--front {
    top: 410px;
    height: 300px;
    background: var(--paper);
  }
  .brand {
    position: absolute;
    left: 60px; top: 124px;
    display: flex; align-items: center; gap: 12px;
  }
  .brand__dot {
    width: 22px; height: 22px; border-radius: 50%;
    background: var(--pink-soft);
  }
  .brand__name {
    font-size: 22px; font-weight: 400; color: var(--ink);
    letter-spacing: .5px;
  }
  .title {
    position: absolute;
    left: 290px; top: 78px;
  }
  .title__tag {
    display: inline-block;
    background: linear-gradient(90deg, var(--gold-deep), var(--gold) 60%, #f2c75a);
    color: var(--paper);
    font-size: 18px;
    font-weight: 400;
    letter-spacing: 2px;
    padding: 2px 14px;
    margin-bottom: 6px;
  }
  .title__line {
    display: block;
    color: var(--pink);
    font-size: 52px;
    line-height: 1.05;
    font-weight: 400;
  }
  .roller-art {
    position: absolute;
    left: 540px; top: 50px;
    width: 200px; height: 200px;
    border-radius: 50%;
    background: linear-gradient(135deg, #f3a6cd 0%, #f6c7c0 55%, #fbefb0 100%);
  }
  .dot-field {
    position: absolute;
    left: 740px; top: 40px;
    width: 230px; height: 220px;
    background: linear-gradient(90deg, rgba(216,154,28,.06), rgba(216,154,28,.16));
  }
  .depth {
    position: absolute;
    right: 60px; top: 110px;
    color: var(--gold-deep);
    text-align: right;
  }
  .depth__value { font-size: 24px; font-weight: 600; }
  .depth__unit { font-weight: 400; font-size: 20px; }
  .depth__label { display: block; font-size: 14px; }

  /* Side panel – benefits and caution */
  .panel--benefits {
    top: 730px;
    height: 300px;
    background: linear-gradient(90deg, var(--cream) 0%, var(--pink-pale) 55%, var(--pink-soft) 100%);
  }
  .benefits {
    position: absolute;
    left: 40px; right: 40px; top: 40px;
    display: flex;
    justify-content: space-around;
    align-items: flex-start;
  }
  .benefit {
    display: flex; flex-direction: column; align-items: center; gap: 14px;
    width: 200px; text-align: center;
    font-size: 17px; line-height: 1.3;
  }
  .benefit__mark {
    width: 40px; height: 40px; border-radius: 50%;
    background: var(--pink);
    opacity: .75;
  }
  .caution {
    position: absolute;
    left: 60px; right: 60px; bottom: 34px;
    font-size: 13px;
    line-height: 1.45;
    color: var(--ink);
    text-align: center;
  }
  .caution__label {
    font-weight: 600;
    color: var(--gold-deep);
    letter-spacing: 1px;
  }
</style>
</head>
<body>

  <section class="panel panel--features" aria-label="Product features">
    <div class="product-photo" role="img" aria-label="Photo of the derma roller with black roller head and clear handle"></div>
    <svg class="callouts" viewBox="0 0 1000 240" aria-hidden="true">
      <g fill="none" stroke="#d89a1c" stroke-width="2">
        <line x1="262" y1="70" x2="292" y2="90"/>
        <line x1="262" y1="120" x2="292" y2="120"/>
        <line x1="262" y1="170" x2="292" y2="150"/>
        <line x1="708" y1="90" x2="750" y2="70"/>
        <line x1="708" y1="150" x2="750" y2="172"/>
      </g>
    </svg>
    <p class="feature feature--needles">540 high quality titanium needles</p>
    <p class="feature feature--tips">Ultra sharp needle tips</p>
    <p class="feature feature--arrangement">Crossline needle arrangement</p>
    <p class="feature feature--handle">Ergonomic handle</p>
    <p class="feature feature--grip">Anti slip grip</p>
  </section>

  <section class="panel panel--front" aria-label="Front panel">
    <div class="brand">
      <span class="brand__dot"></span>
      <span class="brand__name">Velvet Glow Co.</span>
    </div>
    <h1 class="title">
      <span class="title__tag">COSMETIC</span>
      <span class="title__line">DERMA</span>
      <span class="title__line">ROLLER</span>
    </h1>
    <div class="roller-art" role="img" aria-label="Line illustration of a derma roller over a pink-to-yellow circle"></div>
    <div class="dot-field" role="img" aria-label="Gold dot pattern"></div>
    <p class="depth">
      <span class="depth__value">0.25<span class="depth__unit">mm</span></span>
      <span class="depth__label">microneedle</span>
    </p>
  </section>

  <section class="panel panel--benefits" aria-label="Benefits and caution">
    <div class="benefits">
      <div class="benefit"><span class="benefit__mark"></span>Skin Rejuvenation</div>
      <div class="benefit"><span class="benefit__mark"></span>Collagen Induction Therapy</div>
      <div class="benefit"><span class="benefit__mark"></span>Increase product absorption</div>
      <div class="benefit"><span class="benefit__mark"></span>Reduce acne scars and pigmentation</div>
    </div>
    <p class="caution">
      <span class="caution__label">CAUTION</span> – For personal use only. Do not use if allergic to metal.
      Do not use on open skin, wounds or active acne. Sterilise roller before and after use.
    </p>
  </section>

</body>
</html>
```